Service Offering

We need a brochure for our financial advisers, the brochure is specifically for clients of an accounting firm. We provide insurance solutions for the accounting firm, but all they will do to generate new business for us is hand their client the brochure. So we will reply on the brochure to convey our service offering. We are in the process of re-branding and we need something fresh and interesting as we are!! Link to our new demo site below:
http://preview.velmora.co.nz/lumen/

This should allow for an idea of our feel. I'll also attach our logo and a powerpoint that we did for them to gain their trust this captures most of what we are offering their clients, shout if you have any questions, thanks

Accounting

```html
<!DOCTYPE html>
<html lang="en">
<head>
<meta charset="utf-8">
<title>Lumen — Service Offering Brochure Cover</title>
<link rel="stylesheet" href="https://fonts.googleapis.com/css2?family=Josefin+Sans:wght@300;400&display=swap">
<style>
  :root {
    --stage: #9a9a9a;
    --sky-top: #8a7f98;
    --sky-mid: #b89aa8;
    --sun-glow: #f6d49a;
    --horizon: #d99a55;
    --field-light: #c98a3e;
    --field-dark: #6e4318;
    --panel: rgba(58, 54, 62, 0.55);
    --ink-light: #ffffff;
  }
  * { box-sizing: border-box; margin: 0; padding: 0; }
  html, body {
    width: 1200px;
    height: 900px;
    overflow: hidden;
    background: var(--stage);
  }
  .brochure-cover {
    position: absolute;
    left: 100px;
    top: 97px;
    width: 1000px;
    height: 706px;
    overflow: hidden;
    box-shadow: 0 14px 30px rgba(0, 0, 0, 0.25);
  }
  .cover-photo {
    position: absolute;
    inset: 0;
    background:
      radial-gradient(ellipse 30% 22% at 44% 56%, var(--sun-glow) 0%, rgba(246, 212, 154, 0) 100%),
      linear-gradient(180deg,
        var(--sky-top) 0%,
        var(--sky-mid) 32%,
        var(--horizon) 50%,
        var(--field-light) 62%,
        var(--field-dark) 100%);
  }
  .brand-panel {
    position: absolute;
    left: 60px;
    top: 70px;
    width: 350px;
    height: 535px;
    background: var(--panel);
  }
  .frame-line {
    position: absolute;
    inset: 0;
    pointer-events: none;
  }
  .brand-lockup {
    position: absolute;
    left: 90px;
    top: 472px;
    display: flex;
    flex-direction: column;
    gap: 8px;
    color: var(--ink-light);
    font-family: "Josefin Sans", sans-serif;
    font-weight: 300;
  }
  .brand-name {
    font-size: 50px;
    line-height: 1;
    letter-spacing: 2px;
  }
  .brand-tagline {
    font-size: 12px;
    letter-spacing: 1px;
  }
</style>
</head>
<body>
  <main class="brochure-cover">
    <div class="cover-photo" role="img" aria-label="Photograph of two people standing in a golden grass field at sunset under a cloudy purple sky"></div>
    <div class="brand-panel"></div>
    <svg class="frame-line" width="1000" height="706" viewBox="0 0 1000 706" aria-hidden="true">
      <polyline points="430,62 930,62 930,390" fill="none" stroke="#ffffff" stroke-width="1.5"/>
    </svg>
    <div class="brand-lockup">
      <span class="brand-name">lumen</span>
      <span class="brand-tagline">cover for every season</span>
    </div>
  </main>
</body>
</html>
```